Can You Help Sell Glass Cabinets with a Banner Ad?

Our New Zealand-based company designs and sells glass cabinets and display cases. 75% of our customers are other businesses who want to display products in their shop or showroom. The other 25% of our customers are householders who want a glass cabinet for their personal collectables. We have been trading 2 years now, and are expanding rapidly. Our website address is www.vitrinaplace.example.nz.
We have made a strategic decision to focus on online advertising this year. This is because we want to raise our profile to the greatest number of and widest range of people. For now, this means banner advertising on high traffic New Zealand-based websites in an attempt to generate more traffic to our website. The websites we will initially use are www.ploverpost.example.nz and www.tuidaily.example.nz.
We therefore need a set of eye-catching banner ads designed for our online marketing campaign. The three banners required will probably just be variations on a single design.

Banner 1: Top Banner
760x120

Banner 2: Skyscraper
160x600

Banner 3: Medium Rectangle
300x250

Target Market(s)

The primary target market will be retailers who have shops and showrooms. They may not yet know they need a showcase.

Industry/Entity Type

Advertising

Requirements
Must have
• Vitrina Place logo
"High quality glass cabinets and showcases"
Maybe also "Show your products, not the cabinet"
[Corporate colour is green, as per logo. Secondary colours are orange, purple and grey.]
[Please use New Zealand (British) spelling]

Nice to have
• Please view our website and brochure on the Resources page for the look and feel of our company. In particular we like our logo, so it is possible you can take a lead from this. The logo emblem is designed to be evocative of glass.
The logo spot colour is 41,0,70,10.

```html
<!DOCTYPE html>
<html lang="en-NZ">
<head>
<meta charset="utf-8">
<title>Vitrina Place – banner set</title>
<link rel="stylesheet" href="https://fonts.googleapis.com/css2?family=Nunito+Sans:ital,wght@0,400;0,600;0,700;1,400&display=swap">
<style>
  :root {
    --page: #ffffff;
    --green: #c6e06a;
    --brown-light: #8d7b6b;
    --brown-dark: #4f3f33;
    --ink: #4e3d2f;
    --ink-soft: #5b4a3c;
    --button-brown: #5a4535;
    --button-purple: #4b3550;
    --white: #ffffff;
    --glass-light: #eef3e4;
    --glass-mid: #c9d3c2;
    --glass-base: #9c958f;
  }
  html, body {
    margin: 0;
    width: 1200px;
    height: 1140px;
    overflow: hidden;
    background: var(--page);
    font-family: "Nunito Sans", "Helvetica Neue", Arial, sans-serif;
  }
  .stage {
    position: relative;
    width: 800px;
    height: 760px;
    transform: scale(1.5);
    transform-origin: 0 0;
  }
  .banner {
    position: absolute;
    overflow: hidden;
    background: var(--green);
  }
  .banner-band {
    position: absolute;
    inset: 0;
  }
  .skyscraper { left: 16px; top: 13px; width: 160px; height: 600px; }
  .rectangle  { left: 189px; top: 363px; width: 300px; height: 250px; }
  .leaderboard { left: 16px; top: 626px; width: 760px; height: 120px; }

  .brand-mark {
    position: absolute;
    background: rgba(255,255,255,0.55);
  }
  .brand-name {
    position: absolute;
    margin: 0;
    color: var(--white);
    font-weight: 700;
    letter-spacing: 0.2px;
    white-space: nowrap;
    text-transform: uppercase;
  }
  .brand-tagline {
    position: absolute;
    margin: 0;
    color: var(--white);
    font-weight: 400;
    white-space: nowrap;
  }
  .headline {
    position: absolute;
    margin: 0;
    color: var(--ink);
    font-weight: 600;
    font-size: 20.5px;
    line-height: 24px;
    letter-spacing: -0.2px;
  }
  .subline {
    position: absolute;
    margin: 0;
    color: var(--ink-soft);
    font-style: italic;
    font-size: 13.5px;
    line-height: 17px;
  }
  .cta {
    position: absolute;
    display: flex;
    align-items: center;
    justify-content: center;
    height: 22px;
    border-radius: 6px;
    color: var(--white);
    font-size: 12.5px;
    font-weight: 600;
    background: var(--button-brown);
  }
  .cta--purple { background: var(--button-purple); }
  .product-shot {
    position: absolute;
    border-radius: 2px;
  }
  .product-shot--tall {
    background: linear-gradient(180deg, var(--glass-light) 0%, var(--glass-mid) 85%, var(--glass-base) 100%);
  }
  .product-shot--lit {
    background: radial-gradient(ellipse at 60% 45%, #f7f9e6 0%, #dfe6b8 60%, #8b8a60 100%);
  }
  .product-shot--counter {
    background: linear-gradient(90deg, rgba(238,240,238,0) 0%, #e9ecea 15%, #d6dbd8 60%, #c3c8c6 100%);
  }
</style>
</head>
<body>
<main class="stage">

  <!-- Skyscraper 160x600 -->
  <section class="banner skyscraper" aria-label="Vitrina Place skyscraper banner">
    <svg class="banner-band" width="160" height="600" viewBox="0 0 160 600" aria-hidden="true">
      <defs>
        <linearGradient id="sky-brown" x1="0" y1="0" x2="0" y2="1">
          <stop offset="0" stop-color="#8d7b6b"/>
          <stop offset="1" stop-color="#4f3f33"/>
        </linearGradient>
      </defs>
      <polygon points="0,0 160,0 160,70 48,143 0,113" fill="url(#sky-brown)"/>
      <polyline points="0,113 48,143 160,70" fill="none" stroke="#ffffff" stroke-width="3"/>
    </svg>
    <span class="brand-mark" style="left:10px; top:6px; width:32px; height:32px;"></span>
    <p class="brand-name" style="left:8px; top:47px; font-size:14.5px;">Vitrina Place</p>
    <p class="brand-tagline" style="left:8px; top:65px; font-size:10.5px;">design strength value</p>

    <h2 class="headline" style="left:7px; top:162px; width:150px;">High quality glass cabinets and showcases</h2>
    <p class="subline" style="left:9px; top:247px; width:150px;">Show your products, not the cabinet</p>
    <span class="cta cta--purple" style="left:9px; top:294px; width:93px;">Learn more</span>

    <div class="product-shot product-shot--tall" role="img" aria-label="Photo of a tall frameless glass display cabinet with shelves" style="left:25px; top:339px; width:115px; height:241px;"></div>
  </section>

  <!-- Medium rectangle 300x250 -->
  <section class="banner rectangle" aria-label="Vitrina Place medium rectangle banner">
    <svg class="banner-band" width="300" height="250" viewBox="0 0 300 250" aria-hidden="true">
      <defs>
        <linearGradient id="rect-brown" x1="0" y1="0" x2="0" y2="1">
          <stop offset="0" stop-color="#8d7b6b"/>
          <stop offset="1" stop-color="#4f3f33"/>
        </linearGradient>
      </defs>
      <polygon points="0,0 300,0 300,12 0,172" fill="url(#rect-brown)"/>
      <line x1="300" y1="12" x2="0" y2="172" stroke="#ffffff" stroke-width="3"/>
    </svg>
    <span class="brand-mark" style="left:8px; top:10px; width:34px; height:34px;"></span>
    <p class="brand-name" style="left:54px; top:7px; font-size:19px;">Vitrina Place</p>
    <p class="brand-tagline" style="left:54px; top:32px; font-size:13.5px;">design strength value</p>

    <div class="product-shot product-shot--lit" role="img" aria-label="Photo of a lit glass display cabinet with black frame" style="left:20px; top:97px; width:105px; height:135px;"></div>

    <h2 class="headline" style="left:141px; top:95px; width:155px;">High quality glass cabinets and showcases</h2>
    <p class="subline" style="left:142px; top:171px; width:150px;">Show your products, not the cabinet</p>
    <span class="cta" style="left:141px; top:212px; width:93px;">Learn more</span>
  </section>

  <!-- Top banner 760x120 -->
  <section class="banner leaderboard" aria-label="Vitrina Place top banner">
    <svg class="banner-band" width="760" height="120" viewBox="0 0 760 120" aria-hidden="true">
      <defs>
        <linearGradient id="lead-brown" x1="0" y1="0" x2="0" y2="1">
          <stop offset="0" stop-color="#8d7b6b"/>
          <stop offset="1" stop-color="#4f3f33"/>
        </linearGradient>
      </defs>
      <polygon points="0,0 264,0 279,52 252,120 0,120" fill="url(#lead-brown)"/>
      <polyline points="264,0 279,52 252,120" fill="none" stroke="#ffffff" stroke-width="3"/>
    </svg>
    <span class="brand-mark" style="left:8px; top:41px; width:34px; height:34px;"></span>
    <p class="brand-name" style="left:57px; top:39px; font-size:19.5px;">Vitrina Place</p>
    <p class="brand-tagline" style="left:57px; top:62px; font-size:14px;">design strength value</p>

    <h2 class="headline" style="left:294px; top:9px; width:250px;">High quality glass cabinets and showcases</h2>
    <p class="subline" style="left:294px; top:61px; width:250px;">Show your products, not the cabinet</p>
    <span class="cta" style="left:294px; top:89px; width:91px;">Learn more</span>

    <div class="product-shot product-shot--counter" role="img" aria-label="Photo of a modular glass counter and tower showcase layout" style="left:540px; top:5px; width:220px; height:115px;"></div>
  </section>

</main>
</body>
</html>
```